Looking for a modern website banner design

Bramblecrest Coaching Partners looking for the development of the main banner of the website. The project description and photos are included in the upload files.

```html
<!DOCTYPE html>
<html lang="en">
<head>
<meta charset="utf-8">
<title>Bramblecrest Coaching Partners – Website Banner</title>
<link rel="stylesheet" href="https://fonts.googleapis.com/css2?family=Cabin:ital,wght@0,400;0,600;0,700;1,400&display=swap">
<style>
  :root {
    --page-bg: #d9d9db;
    --panel-black: #000000;
    --accent-blue: #1f72b6;
    --stripe-blue: #6aaee4;
    --light-grey: #ececec;
    --white: #ffffff;
    --photo-red: #b3202c;
    --photo-dark: #1b1b1d;
  }
  * { box-sizing: border-box; margin: 0; padding: 0; }
  html, body {
    width: 1200px; height: 649px; overflow: hidden;
    background: var(--page-bg);
    font-family: "Cabin", "Gill Sans", sans-serif;
  }
  .banner {
    position: absolute; left: 81px; top: 69px;
    width: 1038px; height: 486px;
    overflow: hidden;
    background: var(--light-grey);
  }
  .banner-shapes { position: absolute; inset: 0; width: 100%; height: 100%; }
  .athlete-photo {
    position: absolute; left: 38px; top: 24px;
    width: 262px; height: 462px;
    border-radius: 4px 4px 0 0;
    background: linear-gradient(180deg, var(--photo-dark) 0%, var(--photo-red) 45%, var(--photo-dark) 75%, #111 100%);
  }
  .brand {
    position: absolute; right: 72px; top: 54px;
    display: flex; align-items: center; gap: 10px;
    color: var(--white);
    font-weight: 600; font-size: 19px; line-height: 22px;
    text-align: left;
  }
  .brand-dot {
    width: 34px; height: 34px; border-radius: 50%;
    background: var(--accent-blue);
    flex: none;
  }
  .quote-mark {
    position: absolute; left: 590px; top: 136px;
    width: 44px; text-align: center;
    color: var(--accent-blue);
    font-weight: 700; font-size: 86px; line-height: 86px;
  }
  .testimonial {
    position: absolute; left: 361px; top: 203px; width: 580px;
    color: var(--white);
    font-style: italic; font-weight: 400;
    font-size: 22px; line-height: 29.5px;
  }
  .testimonial sup { font-size: 11px; font-style: normal; }
  .attribution {
    position: absolute; left: 756px; top: 349px;
    color: var(--white);
    font-size: 16.5px; line-height: 20px;
  }
  .attribution-name {
    color: var(--accent-blue); font-weight: 700; font-size: 17px;
    margin-bottom: 1px;
  }
</style>
</head>
<body>
  <main class="banner">
    <svg class="banner-shapes" viewBox="0 0 1920 900" preserveAspectRatio="none" aria-hidden="true">
      <defs>
        <linearGradient id="left-fade" x1="0" y1="0" x2="1" y2="0">
          <stop offset="0" stop-color="#e6e6e6"/>
          <stop offset="1" stop-color="#f7f7f7"/>
        </linearGradient>
        <linearGradient id="stripe-fade" x1="0" y1="0" x2="0" y2="1">
          <stop offset="0" stop-color="#5aa4e0"/>
          <stop offset="0.5" stop-color="#a9d0f0"/>
          <stop offset="1" stop-color="#ffffff" stop-opacity="0"/>
        </linearGradient>
        <linearGradient id="corner-fade" x1="0" y1="1" x2="0" y2="0">
          <stop offset="0" stop-color="#6aaee4"/>
          <stop offset="1" stop-color="#d6e8f6"/>
        </linearGradient>
      </defs>
      <rect class="left-backdrop" width="1920" height="900" fill="url(#left-fade)"/>
      <polygon class="top-stripe" points="658,0 708,0 330,900 280,900" fill="url(#stripe-fade)"/>
      <polygon class="dark-panel" points="745,0 1920,0 1920,577 1762,900 100,900" fill="var(--panel-black)"/>
      <polygon class="corner-white" points="1920,577 1920,900 1762,900" fill="#ffffff"/>
      <polygon class="corner-stripe" points="1920,640 1920,720 1835,900 1790,900" fill="url(#corner-fade)"/>
      <polygon class="corner-grey" points="1920,720 1920,900 1835,900" fill="#e6e6e6"/>
      <g class="quote-frame" fill="none" stroke="var(--accent-blue)" stroke-width="4">
        <path d="M670 330 H1072"/>
        <path d="M1177 330 H1765 Q1790 330 1790 355 V645 Q1790 670 1765 670 H1615"/>
        <path d="M1375 670 H500"/>
      </g>
    </svg>

    <div class="athlete-photo" role="img" aria-label="Photo of a hockey player in a red and black jersey celebrating with arms raised, stick in hand"></div>

    <div class="brand">
      <span class="brand-dot"></span>
      <span class="brand-name">Bramblecrest<br>Coaching Partners</span>
    </div>

    <div class="quote-mark">“</div>

    <p class="testimonial">Bramblecrest has provided support that has allowed me to develop as a person and an athlete. The P.A.C.E.<sup>™</sup> process allowed me to stay focused on attainable goals each season and progress from Junior to College and now Professional Hockey.</p>

    <div class="attribution">
      <p class="attribution-name">Marcus Delorne</p>
      <p>Riverton Gales</p>
      <p>Atlantic Pro Hockey League</p>
    </div>
  </main>
</body>
</html>
```